Card design for orthopaedic surgeons working as The Meridale Orthopaedic Clinic

Business cards, letterhead

Colors

Designer to choose colors to be used in the design.

Requirements
Must have
• Late addition.
• Cards letterhead must have logos of
• Corvane Federated Guild of Surgeons
• Tellmark Orthopaedic Society
Nice to have
• Back of card to have space for appointment time to be added by hand and some blank space for writing incidental other notes.

```html
<!DOCTYPE html>
<html lang="en">
<head>
<meta charset="UTF-8">
<title>The Meridale Orthopaedic Clinic — Business Card</title>
<link href="https://fonts.googleapis.com/css2?family=Montserrat:wght@400;500;700&display=swap" rel="stylesheet">
<style>
  :root {
    --navy: #0d2a42;
    --navy-deep: #0a2238;
    --sky: #1fa6e0;
    --sky-light: #3aa9ee;
    --paper: #f3f4f6;
    --paper-shade: #dfe2e6;
    --ink: #0f2b45;
    --rule: #9aa3ad;
  }
  * { margin: 0; padding: 0; box-sizing: border-box; }
  html, body { width: 1200px; height: 1200px; overflow: hidden; }
  body {
    background: var(--navy);
    font-family: "Montserrat", sans-serif;
    color: var(--ink);
    position: relative;
  }
  .card {
    position: absolute;
    left: 160px;
    width: 880px;
    height: 502px;
    overflow: hidden;
    background: var(--paper);
    box-shadow: 0 14px 34px rgba(0,0,0,0.35);
  }
  .card--front { top: 70px; }
  .card--back { top: 628px; }
  .card__art { position: absolute; inset: 0; width: 100%; height: 100%; }

  .brand-vertical {
    position: absolute;
    left: 92px;
    top: 251px;
    transform: translate(-50%, -50%) rotate(-90deg);
    white-space: nowrap;
    font-size: 22px;
    font-weight: 400;
    color: var(--sky-light);
    letter-spacing: 0.3px;
  }

  .person {
    position: absolute;
    right: 80px;
    top: 38px;
    text-align: right;
  }
  .person__name {
    font-size: 31px;
    font-weight: 400;
    color: var(--ink);
    padding-bottom: 4px;
    border-bottom: 2px solid var(--rule);
  }
  .person__name strong { font-weight: 700; }
  .person__title {
    font-size: 18px;
    font-weight: 400;
    margin-top: 6px;
  }

  .icon {
    position: absolute;
    width: 34px;
    height: 34px;
  }
  .icon--person { right: 30px; top: 50px; }

  .contacts {
    position: absolute;
    right: 30px;
    top: 340px;
    list-style: none;
  }
  .contacts li {
    display: flex;
    align-items: center;
    justify-content: flex-end;
    gap: 14px;
    height: 50px;
    font-size: 22px;
    font-weight: 400;
  }
  .contacts .icon { position: static; }

  .brand-stack {
    position: absolute;
    left: 34px;
    top: 92px;
    font-size: 36px;
    font-weight: 700;
    line-height: 1.6;
    color: var(--navy);
  }
  .brand-stack span { display: block; }
</style>
</head>
<body>

  <section class="card card--front" aria-label="Business card front">
    <svg class="card__art" viewBox="0 0 880 502" preserveAspectRatio="none" aria-hidden="true">
      <defs>
        <linearGradient id="paperFront" x1="0" y1="0" x2="1" y2="1">
          <stop offset="0" stop-color="#f7f8f9"/>
          <stop offset="0.5" stop-color="#eceef1"/>
          <stop offset="1" stop-color="#f5f6f7"/>
        </linearGradient>
      </defs>
      <rect width="880" height="502" fill="url(#paperFront)"/>
      <path class="band-blue" d="M245 0 H285 C225 90 215 180 268 280 C312 360 365 440 440 502 H305 C298 420 268 335 228 252 C188 170 195 80 245 0Z" fill="#1fa6e0"/>
      <path class="band-navy" d="M0 0 H245 C195 80 188 170 228 252 C268 335 298 420 305 502 H0Z" fill="#0d2a42"/>
    </svg>

    <div class="brand-vertical">The Meridale Orthopaedic Clinic</div>

    <div class="person">
      <div class="person__name">Dr. <strong>Lorem</strong> Ipsum</div>
      <div class="person__title">MS (Ortho), MBBS</div>
    </div>
    <svg class="icon icon--person" viewBox="0 0 34 34" aria-hidden="true">
      <circle cx="17" cy="17" r="17" fill="#0d2a42"/>
      <circle cx="17" cy="13" r="5" fill="#fff"/>
      <path d="M8 26 C9 19 25 19 26 26Z" fill="#fff"/>
    </svg>

    <ul class="contacts">
      <li>+966 44 61207 248
        <svg class="icon" viewBox="0 0 34 34" aria-hidden="true">
          <circle cx="17" cy="17" r="17" fill="#0d2a42"/>
          <rect x="12" y="8" width="10" height="18" rx="2" fill="none" stroke="#fff" stroke-width="1.8"/>
          <line x1="15.5" y1="23" x2="18.5" y2="23" stroke="#fff" stroke-width="1.5"/>
        </svg>
      </li>
      <li>meridaleclinic@postmark.test
        <svg class="icon" viewBox="0 0 34 34" aria-hidden="true">
          <circle cx="17" cy="17" r="17" fill="#0d2a42"/>
          <rect x="9" y="11" width="16" height="12" fill="none" stroke="#fff" stroke-width="1.6"/>
          <path d="M9 11 L17 18 L25 11" fill="none" stroke="#fff" stroke-width="1.6"/>
        </svg>
      </li>
      <li>218 Harlow Lane, US
        <svg class="icon" viewBox="0 0 34 34" aria-hidden="true">
          <circle cx="17" cy="17" r="17" fill="#0d2a42"/>
          <path d="M17 27 C12 20 11 17 11 14 A6 6 0 0 1 23 14 C23 17 22 20 17 27Z" fill="#fff"/>
          <circle cx="17" cy="14" r="2.3" fill="#0d2a42"/>
        </svg>
      </li>
    </ul>
  </section>

  <section class="card card--back" aria-label="Business card back">
    <svg class="card__art" viewBox="0 0 880 502" preserveAspectRatio="none" aria-hidden="true">
      <defs>
        <linearGradient id="paperBack" x1="0" y1="0" x2="1" y2="1">
          <stop offset="0" stop-color="#f7f8f9"/>
          <stop offset="0.5" stop-color="#eceef1"/>
          <stop offset="1" stop-color="#f5f6f7"/>
        </linearGradient>
      </defs>
      <rect width="880" height="502" fill="url(#paperBack)"/>
      <path class="band-blue" d="M600 0 H880 V502 H295 C385 470 425 400 445 300 C465 180 525 80 600 0Z" fill="#1fa6e0"/>
    </svg>
    <svg class="card__art" viewBox="0 0 880 502" preserveAspectRatio="none" role="img" aria-label="Collage of medical imaging panels showing a skeleton, spine, hip and hand joints glowing in blue with red pain highlights">
      <defs>
        <linearGradient id="imaging" x1="0" y1="0" x2="1" y2="1">
          <stop offset="0" stop-color="#4b6fc9"/>
          <stop offset="0.45" stop-color="#1e3a9a"/>
          <stop offset="0.75" stop-color="#2a2f86"/>
          <stop offset="1" stop-color="#182a66"/>
        </linearGradient>
      </defs>
      <path d="M690 0 H880 V502 H505 C530 440 545 360 550 280 C560 170 610 70 690 0Z" fill="url(#imaging)"/>
    </svg>

    <div class="brand-stack">
      <span>The Meridale</span>
      <span>Orthopaedic Clinic</span>
    </div>
  </section>

</body>
</html>
```